Brisk Tide needs a web page for E-commerce site

Small startup business looking for a custom website for my New Saltwater apparel Co.

COMPANY OVERVIEW

Brisk Tide was founded In Mont Belvieu, Tx, right on the heart of pelican cove.

Brisk Tide is the adrenaline, sweat pumping moment you find yourself setting the hook on a monster fish. This is the moment when all your senses come to life as you work to land that trophy, and after a grueling fight when your hi-fiving your fishing buddies...It's that moment... when the waters and the air around you are Brisk Sweet....All or Nothing...pure Addiction......This is BRISK TIDE

Looking for a sharp clean sexy web page for my ecommerce page

I like the look of black background websites.

www.brisktidegear.example
Updates

I am using bigcommerce as my host site if that means anything to y'all

Thank you all for the submissions! There were some great ones!  I will have more projects in the future. thanks again

Target Market(s)

inshore/offshore fishing, saltwater enthusiast

Industry/Entity Type

Business

Requirements
Must have
• logo's

inshore/offshore fishing appeal

compatible with bigcommerce site

```html
<!DOCTYPE html>
<html lang="en">
<head>
<meta charset="utf-8">
<title>Brisk Tide — Saltwater Apparel</title>
<link href="https://fonts.googleapis.com/css2?family=Roboto+Condensed:wght@400;500&family=PT+Sans:wght@400;700&display=swap" rel="stylesheet">
<style>
  :root {
    --page-bg: #161616;
    --topbar: #262626;
    --topbar-line: #3c3c3c;
    --ink-light: #ffffff;
    --ink-muted: #c9c9c9;
    --panel: #000000;
    --sky-top: #8fdcfb;
    --sky-bottom: #4fb9ef;
    --sky-line: #77c8ee;
    --nav-ink: #163a52;
    --accent: #7fd3fa;
    --footer-ink: #1d3f58;
    --footer-link: #2d5877;
    --band: rgba(40, 40, 40, 0.85);
    --social: #1d3a5c;
  }
  * { box-sizing: border-box; margin: 0; padding: 0; }
  html, body { width: 1022px; height: 1200px; overflow: hidden; }
  body {
    position: relative;
    background: radial-gradient(ellipse at 50% 40%, #262626 0%, var(--page-bg) 70%);
    font-family: "PT Sans", sans-serif;
    color: var(--ink-light);
  }
  ul { list-style: none; }

  /* Top utility bar */
  .utility-bar {
    position: absolute; top: 0; left: 0; width: 1022px; height: 36px;
    background: var(--topbar); border-bottom: 1px solid var(--topbar-line);
  }
  .utility-bar ul { position: absolute; right: 100px; top: 0; display: flex; height: 36px; }
  .utility-bar li {
    font-family: "Roboto Condensed", sans-serif; font-size: 11px; color: var(--ink-muted);
    line-height: 36px; padding: 0 9px; border-left: 1px solid var(--topbar-line);
  }
  .utility-bar li:first-child { border-left: none; }

  /* Header */
  .brand {
    position: absolute; left: 80px; top: 62px;
    font-family: "Roboto Condensed", sans-serif; font-weight: 500; font-size: 46px;
    color: var(--ink-light); letter-spacing: 1px; line-height: 1;
  }
  .search {
    position: absolute; left: 692px; top: 99px; width: 252px; height: 28px;
    background: #1f1f1f; border: 1px solid #3a3a3a; display: flex;
  }
  .search span { flex: 1; font-size: 11px; font-style: italic; color: #9a9a9a; line-height: 26px; padding-left: 11px; }
  .search .search-btn { width: 26px; height: 26px; background: var(--accent); display: flex; align-items: center; justify-content: center; }

  /* Main navigation */
  .main-nav {
    position: absolute; left: 76px; top: 143px; width: 869px; height: 46px;
    background: linear-gradient(var(--sky-top), var(--sky-bottom));
  }
  .main-nav ul { display: flex; height: 46px; }
  .main-nav li {
    font-family: "Roboto Condensed", sans-serif; font-size: 16px; color: var(--nav-ink);
    line-height: 46px; padding: 0 20px; border-right: 1px solid var(--sky-line);
  }
  .main-nav li:last-child { border-right: none; }

  /* Hero */
  .hero {
    position: absolute; left: 80px; top: 198px; width: 865px; height: 306px;
    background: linear-gradient(100deg, #d7d7d7 0%, #f4f4f4 35%, #ebebeb 65%, #d5d5d5 100%);
  }
  .slider-arrows {
    position: absolute; right: 0; bottom: 0; width: 50px; height: 40px;
    background: rgba(255,255,255,0.55); display: flex; align-items: center; justify-content: center;
  }

  /* Content panel */
  .content {
    position: absolute; left: 76px; top: 504px; width: 869px; height: 437px; background: var(--panel);
  }
  .category-card {
    position: absolute; top: 16px; width: 269px; height: 157px; border: 1px solid #3a3a3a; overflow: hidden;
  }
  .category-card .art { position: absolute; inset: 0; }
  .category-card .label {
    position: absolute; left: 0; bottom: 0; width: 100%; height: 41px; background: var(--band);
    font-family: "Roboto Condensed", sans-serif; font-size: 17px; line-height: 41px; padding-left: 18px; letter-spacing: 0.3px;
  }
  .card-outwear { left: 19px; }
  .card-outwear .art { background: linear-gradient(90deg, #d9d9d9, #3a2e22 30%, #2c231a 70%, #dcdcdc); }
  .card-best { left: 302px; }
  .card-best .art { background: linear-gradient(90deg, #e2e2e2, #f7f7f7 45%, #e9e9e9); }
  .card-offers { left: 584px; }
  .card-offers .art { background: linear-gradient(90deg, #e0e0e0, #f1ec92 30%, #f2ee94 70%, #e3e3e3); }

  .welcome { position: absolute; left: 29px; top: 212px; width: 560px; }
  .welcome h1 {
    font-family: "Roboto Condensed", sans-serif; font-weight: 400; font-size: 24px;
    color: var(--accent); letter-spacing: 0.2px; margin-bottom: 10px;
  }
  .welcome .lead { font-size: 13px; font-weight: 700; margin-bottom: 2px; white-space: nowrap; }
  .welcome p { font-size: 11px; line-height: 18.7px; color: #f0f0f0; white-space: nowrap; }
  .welcome p + p { margin-top: 8px; }

  .promo {
    position: absolute; left: 603px; top: 202px; width: 243px; height: 193px;
    border: 1px solid #3a3a3a; overflow: hidden;
    background: linear-gradient(160deg, #5c7a55 0%, #4f6a4c 40%, #2e4a66 75%, #30445c 100%);
  }
  .promo .caption {
    position: absolute; left: 0; bottom: 0; width: 100%; height: 57px;
    background: rgba(40, 55, 75, 0.8); padding: 6px 13px;
  }
  .promo .save { font-family: "Roboto Condensed", sans-serif; font-size: 15px; }
  .promo .save b { font-weight: 400; font-size: 27px; }
  .promo .small { font-size: 10.5px; margin-top: -3px; }

  /* Footer */
  .site-footer {
    position: absolute; left: 76px; top: 941px; width: 869px; height: 239px;
    background: linear-gradient(var(--sky-top), var(--sky-bottom));
    color: var(--footer-ink);
  }
  .footer-col { position: absolute; top: 30px; }
  .footer-col h2 {
    font-family: "Roboto Condensed", sans-serif; font-weight: 400; font-size: 17px; margin-bottom: 6px;
  }
  .footer-col li { font-size: 11.5px; color: var(--footer-link); line-height: 20px; padding-left: 3px; }
  .col-quick { left: 45px; }
  .col-products { left: 203px; }
  .col-sub { left: 355px; top: 32px; }
  .col-support { left: 502px; top: 32px; }
  .col-connect { left: 651px; top: 32px; }
  .social { display: flex; gap: 4px; margin-top: 2px; }
  .social span { width: 24px; height: 24px; border-radius: 50%; background: var(--social); }
  .payments { display: flex; gap: 7px; margin-top: 12px; }
  .payments span { width: 31px; height: 20px; background: #ffffff; border: 1px solid #6a8aa0; }
  .footer-rule { position: absolute; left: 45px; top: 180px; width: 775px; height: 1px; background: #95d6f3; }
  .copyright { position: absolute; left: 47px; top: 194px; font-size: 10.5px; color: var(--footer-link); }
</style>
</head>
<body>
  <nav class="utility-bar" aria-label="Account">
    <ul>
      <li>MY ACCOUNT</li><li>MY WISH LIST</li><li>MY CART</li><li>CHECKOUT</li><li>LOG IN</li>
    </ul>
  </nav>

  <div class="brand">Brisk Tide</div>

  <div class="search">
    <span>Search here</span>
    <div class="search-btn">
      <svg width="16" height="16" viewBox="0 0 16 16"><circle cx="7" cy="7" r="5" fill="none" stroke="#1d4a6a" stroke-width="1.5"/><line x1="10.5" y1="10.5" x2="14" y2="14" stroke="#1d4a6a" stroke-width="1.5"/></svg>
    </div>
  </div>

  <nav class="main-nav" aria-label="Main">
    <ul>
      <li>HOME</li><li>ABOUT US</li><li>PRODUCTS</li><li>SHIPPING</li><li>RETURN</li><li>ORDER NOW</li><li>SUPPORT</li><li>CONTACT</li>
    </ul>
  </nav>

  <section class="hero" role="img" aria-label="Two white t-shirts, back with a large teal fish print and front with a small chest logo">
    <div class="slider-arrows">
      <svg width="34" height="22" viewBox="0 0 34 22"><polyline points="11,2 3,11 11,20" fill="none" stroke="#111" stroke-width="1.8"/><polyline points="23,2 31,11 23,20" fill="none" stroke="#111" stroke-width="1.8"/></svg>
    </div>
  </section>

  <main class="content">
    <div class="category-card card-outwear">
      <div class="art" role="img" aria-label="Black t-shirts, back and front"></div>
      <div class="label">LATEST OUTWEAR</div>
    </div>
    <div class="category-card card-best">
      <div class="art" role="img" aria-label="White t-shirts with teal fish print"></div>
      <div class="label">BEST SELLING</div>
    </div>
    <div class="category-card card-offers">
      <div class="art" role="img" aria-label="Yellow t-shirts with blue marlin print"></div>
      <div class="label">SPECIAL OFFERS</div>
    </div>

    <article class="welcome">
      <h1>WELCOME TO OUR WEBSITE MAINPAGE</h1>
      <div class="lead">Mauris vel lacus vitae felis vestibulum volutpat. Etiam est nunc, venenatis in, tristique eu.</div>
      <p>imperdiet ac, nisl. Cum sociis natoque penatibus et magnis dis parturient montes, nascetur ridiculus<br>&nbsp;Etiam eu urna. Sed porta. Suspendisse quam leo, molestie sed, luctus quis, feugiat in, pede. Fusce tellus. Sed<br>metus augue, convallis et, vehicula ut, pulvinar eu, ante. Integer orci tellus, tristique vitae, consequat nec,<br>porta vel, lectus. Nulla sit amet diam. Duis non nunc.</p>
      <p>Nunc tempus felis vitae urna. Vivamus porttitor, g, purus nisi eleifend libero, a tempus libero lectus feugiat</p>
    </article>

    <aside class="promo" role="img" aria-label="Two anglers fishing by the water">
      <div class="caption">
        <div class="save">NOW SAVE <b>20%</b></div>
        <div class="small">Curabitur vel mi sit amet mag</div>
      </div>
    </aside>
  </main>

  <footer class="site-footer">
    <div class="footer-col col-quick">
      <h2>QUICK LINKS</h2>
      <ul><li>Nunc tempus</li><li>Felis vitae urna</li><li>Vivamus porttitor</li><li>Purus nisi eleifend</li><li>Libero tempus</li></ul>
    </div>
    <div class="footer-col col-products">
      <h2>PRODUCTS</h2>
      <ul><li>Nunc tempus</li><li>Felis vitae urna</li><li>Vivamus porttitor</li><li>Purus nisi eleifend</li><li>Libero tempus</li></ul>
    </div>
    <div class="footer-col col-sub">
      <h2>SUBLINKS</h2>
      <ul><li>Nunc tempus</li><li>Felis vitae urna</li><li>Vivamus porttitor</li><li>Purus nisi eleifend</li><li>Libero tempus</li></ul>
    </div>
    <div class="footer-col col-support">
      <h2>SUPPORT</h2>
      <ul><li>Nunc tempus</li><li>Felis vitae urna</li><li>Vivamus porttitor</li><li>Purus nisi eleifend</li><li>Libero tempus</li></ul>
    </div>
    <div class="footer-col col-connect">
      <h2>GET CONNTED</h2>
      <div class="social" aria-label="Social links"><span></span><span></span><span></span><span></span></div>
      <div class="payments" aria-label="Accepted payments"><span></span><span></span><span></span><span></span><span></span></div>
    </div>
    <div class="footer-rule"></div>
    <div class="copyright">© 2013 Company Name.&nbsp; All right reserved.&nbsp; Term of Use</div>
  </footer>
</body>
</html>
```